Brightpath Holdings Business Card

Create a two sided, high gloss, quality business card for Brightpath Holdings.

Target Market(s)

People wanting to purchase, scale, and sell businesses.

Industry/Entity Type

Entrepreneurs

Contact Information for Business Card

One line: Dana Corwell, CPA, CMA Another line: Entrepreneur & Investor Another line: Business Ownership Transition Expert Another line: Multi-State Licensed Real Estate Broker Phone 954-BRTPATH (278-7284) Email Dana@Brightpath Holdings.com Website www.Brightpath.com

Requirements
Must have
• Black Card, logo on one side, all other information on the other side including a small logo.
Nice to have
• Possibly add a tagline "Helping entrepreneurs live a life they don't need a vacation from"
Should not have
• There will not be a mailing address on these cards.

```html
<!DOCTYPE html>
<html lang="en">
<head>
<meta charset="utf-8">
<title>Brightpath Holdings Business Card</title>
<link href="https://fonts.googleapis.com/css2?family=Arimo:wght@400;700&display=swap" rel="stylesheet">
<style>
  :root {
    --backdrop: #3a3a3b;
    --card: #2a2a2b;
    --card-edge: #8a7433;
    --gold: #d4ad4a;
    --emboss: #5a5a5c;
    --text-light: #f2f2f2;
    --divider: #5c5c5e;
  }
  * { box-sizing: border-box; margin: 0; padding: 0; }
  html, body { width: 1200px; height: 689px; overflow: hidden; }
  body {
    background: var(--backdrop);
    font-family: "Arimo", Arial, sans-serif;
    display: flex;
    align-items: center;
    justify-content: center;
    gap: 40px;
  }
  .card {
    width: 520px;
    height: 297px;
    background: var(--card);
    border: 1.5px solid var(--card-edge);
    border-radius: 16px;
    position: relative;
    overflow: hidden;
  }
  .card--front {
    display: flex;
    align-items: center;
    justify-content: center;
  }
  .brand {
    display: flex;
    align-items: center;
    gap: 10px;
    font-weight: 700;
    white-space: nowrap;
  }
  .brand__dot {
    border-radius: 50%;
    flex: none;
  }
  .card--front .brand { color: var(--emboss); font-size: 36px; }
  .card--front .brand__dot { width: 34px; height: 34px; background: var(--emboss); }

  .card--back {
    display: flex;
    align-items: center;
    padding: 0 26px 0 26px;
  }
  .card--back .brand { color: var(--gold); font-size: 17px; gap: 7px; }
  .card--back .brand__dot { width: 16px; height: 16px; background: var(--gold); }
  .back__logo { width: 195px; display: flex; justify-content: center; margin-top: 70px; }
  .divider {
    width: 1px;
    height: 150px;
    background: var(--divider);
    margin: 0 18px 0 12px;
    align-self: center;
  }
  .details { flex: 1; }
  .details__name {
    color: var(--gold);
    font-weight: 700;
    font-size: 19px;
    margin-bottom: 4px;
    white-space: nowrap;
  }
  .details__titles {
    list-style: none;
    color: var(--text-light);
    font-size: 11.5px;
    line-height: 1.35;
    margin-bottom: 14px;
  }
  .details__contact {
    list-style: none;
    color: var(--text-light);
    font-size: 11.5px;
    line-height: 1.55;
  }
  .details__contact li { display: flex; align-items: center; gap: 8px; white-space: nowrap; }
  .icon { width: 11px; height: 11px; flex: none; fill: var(--gold); }
</style>
</head>
<body>
  <section class="card card--front" aria-label="Card front">
    <div class="brand"><span class="brand__dot"></span>Brightpath Holdings</div>
  </section>

  <section class="card card--back" aria-label="Card back">
    <div class="back__logo">
      <div class="brand"><span class="brand__dot"></span>Brightpath Holdings</div>
    </div>
    <div class="divider"></div>
    <div class="details">
      <h1 class="details__name">Dana Corwell, CPA, CMA</h1>
      <ul class="details__titles">
        <li>Entrepreneur &amp; Investor</li>
        <li>Business Ownership Transition Expert</li>
        <li>Multi-State Licensed Real Estate Broker</li>
      </ul>
      <ul class="details__contact">
        <li>
          <svg class="icon" viewBox="0 0 24 24" aria-hidden="true"><path d="M6.6 10.8a15 15 0 0 0 6.6 6.6l2.2-2.2a1 1 0 0 1 1-.25 11.4 11.4 0 0 0 3.6.57 1 1 0 0 1 1 1V20a1 1 0 0 1-1 1A17 17 0 0 1 3 4a1 1 0 0 1 1-1h3.5a1 1 0 0 1 1 1c0 1.25.2 2.45.57 3.57a1 1 0 0 1-.25 1z"/></svg>
          954-BRTPATH (278-7284)
        </li>
        <li>
          <svg class="icon" viewBox="0 0 24 24" aria-hidden="true"><path d="M2 5h20v14H2z M3 6l9 7 9-7" stroke="#2a2a2b" stroke-width="1.5"/></svg>
          Dana@Brightpath Holdings.com
        </li>
        <li>
          <svg class="icon" viewBox="0 0 24 24" aria-hidden="true"><circle cx="12" cy="12" r="10"/><path d="M2 12h20M12 2c3 3 3 17 0 20M12 2c-3 3-3 17 0 20" stroke="#2a2a2b" stroke-width="1.5" fill="none"/></svg>
          www.Brightpath.com
        </li>
      </ul>
    </div>
  </section>
</body>
</html>
```